Oven Cleaning Business owner needs business card design

Hi there,
Would like for a business card to be designed for myself, the owner of a professional oven cleaning business on the Sunshine Coast.
Would like it to look sleek, and modern-ish. Bit creative is encouraged too.
Include following:
Name/title: Corin ter Haghe, Owner
Phone number: 1300 482 916
Email: info@hearthshinecrew.com.au
Website: www.hearthshinecrew.com.au

```html
<!DOCTYPE html>
<html lang="en">
<head>
<meta charset="utf-8">
<title>Hearthshine Crew – Business Card</title>
<link rel="stylesheet" href="https://fonts.googleapis.com/css2?family=Montserrat:wght@400;500;700;800&display=swap">
<style>
  :root {
    --teal: #52c5cc;
    --ink: #111111;
    --paper: #ffffff;
    --stage: #e9eaec;
  }
  * { margin: 0; padding: 0; box-sizing: border-box; }
  html, body { width: 1200px; height: 887px; overflow: hidden; }
  body {
    background: var(--stage);
    font-family: "Montserrat", Arial, sans-serif;
    color: var(--ink);
    display: flex;
    align-items: center;
    justify-content: center;
    gap: 40px;
  }
  .card {
    position: relative;
    width: 540px;
    height: 310px;
    background: var(--paper);
    border-radius: 22px;
    overflow: hidden;
    box-shadow: 0 6px 18px rgba(0,0,0,0.12);
  }
  /* Front */
  .front {
    display: flex;
    align-items: center;
    justify-content: center;
  }
  .front-brand {
    display: flex;
    align-items: center;
    gap: 14px;
  }
  .brand-dot {
    width: 30px; height: 30px;
    border-radius: 50%;
    background: var(--teal);
  }
  .front-name {
    font-weight: 800;
    font-size: 30px;
    letter-spacing: 2px;
    text-transform: uppercase;
    color: var(--teal);
  }
  /* Back */
  .back-brand {
    position: absolute;
    top: 62px;
    left: 0; right: 0;
    text-align: center;
    font-weight: 800;
    font-size: 38px;
    letter-spacing: 3px;
    text-transform: uppercase;
    color: var(--ink);
    line-height: 1;
  }
  .details {
    position: absolute;
    top: 150px;
    left: 40px;
    right: 30px;
    display: flex;
    align-items: center;
  }
  .holder {
    flex: 0 0 215px;
    text-align: right;
    padding-right: 18px;
  }
  .holder-name {
    font-weight: 700;
    font-size: 18px;
    color: var(--teal);
    text-transform: uppercase;
    letter-spacing: 0.3px;
  }
  .holder-title {
    font-weight: 500;
    font-size: 14px;
    margin-top: 2px;
  }
  .divider {
    width: 2px;
    height: 74px;
    background: var(--teal);
  }
  .contact-list {
    list-style: none;
    padding-left: 16px;
    display: flex;
    flex-direction: column;
    gap: 8px;
  }
  .contact-item {
    display: flex;
    align-items: center;
    gap: 9px;
    font-size: 13px;
    font-weight: 500;
  }
  .contact-item svg { width: 15px; height: 15px; flex: none; }
  .edge-band {
    position: absolute;
    left: 0; right: 0; bottom: 0;
    height: 40px;
  }
</style>
</head>
<body>
  <section class="card front">
    <div class="front-brand">
      <span class="brand-dot"></span>
      <span class="front-name">Hearthshine Crew</span>
    </div>
  </section>

  <section class="card back">
    <div class="back-brand">Hearthshine Crew</div>

    <div class="details">
      <div class="holder">
        <div class="holder-name">Corin ter Haghe</div>
        <div class="holder-title">Owner</div>
      </div>
      <div class="divider"></div>
      <ul class="contact-list">
        <li class="contact-item">
          <svg viewBox="0 0 24 24" fill="var(--teal)"><path d="M6.6 10.8a15.1 15.1 0 0 0 6.6 6.6l2.2-2.2a1 1 0 0 1 1-.25 11.4 11.4 0 0 0 3.6.57 1 1 0 0 1 1 1V20a1 1 0 0 1-1 1A17 17 0 0 1 3 4a1 1 0 0 1 1-1h3.5a1 1 0 0 1 1 1c0 1.25.2 2.45.57 3.57a1 1 0 0 1-.25 1z"/></svg>
          <span>1300 482 916</span>
        </li>
        <li class="contact-item">
          <svg viewBox="0 0 24 24" fill="var(--teal)"><path d="M2 5h20v14H2z" opacity="0.25"/><path d="M2 5h20v14H2V5zm2 2v.5l8 5 8-5V7H4zm16 3l-8 5-8-5v7h16v-7z"/></svg>
          <span>info@hearthshinecrew.com.au</span>
        </li>
        <li class="contact-item">
          <svg viewBox="0 0 24 24" fill="none" stroke="var(--teal)" stroke-width="2"><circle cx="12" cy="12" r="9"/><path d="M3 12h18M12 3c3 3 3 15 0 18M12 3c-3 3-3 15 0 18"/></svg>
          <span>www.hearthshinecrew.com.au</span>
        </li>
      </ul>
    </div>

    <svg class="edge-band" viewBox="0 0 540 40" preserveAspectRatio="none">
      <polygon points="0,31 340,31 336,40 0,40" fill="var(--ink)"/>
      <polygon points="350,22 540,0 540,40 342,40" fill="var(--teal)"/>
    </svg>
  </section>
</body>
</html>
```